Creation of a Velmora website

Velmora is a company% 26 # 233; t% 26 # 233; consulting that accompanies Swiss companies or% 26 # 233; strang% 26 # 232; res in the d% 26 # 233; development of their business on the market% 26 # 233; Switzerland by providing strategic contacts (personalized contact program% 26 # 233; s) or market information% 26 # 233; (% 26 # 233; market research% 26 # 233;) and by providing administrative support (repr% 26 # 233; tax representation) or logistics (organization of% 26 # 233; v% 26 # 233; nement, assistance for participation% 26 # 224; fairs). Our customers are mainly European companies wishing to develop their business in Switzerland. N% 26 # 233; however, our services are% 26 # 233; also aimed at Swiss companies wishing to develop in other parts of Switzerland. Our site must therefore be% 26 # 234; capable of being translated into several languages. The services offered% 26 # 233; s by Velmora may also% 26 # 233; also% 26 # 39;% 26 # 233; tender% 26 # 224; promoting tourism in Switzerland for countries or regions% 26 # 233; foreigners or% 26 # 224; the promotion of trade fairs or fairs with% 26 # 232; sd% 26 # 39; companies of the sectors concerned% 26 # 233; s. It is therefore n% 26 # 233; necessary to be able to add sub-headings of services which can% 26 # 234; be displayed% 26 # 233; es or hide% 26 # 233; es as required. We are 2 associates% 26 # 233; s, low% 26 # 233; s in the French-speaking parts (Neuch% 26 # 226; tel) and al% 26 # 233; manique (Zurich) of Switzerland.

Target Market(s)

Swiss or European companies wishing to develop their activities in Switzerland.

Coding

Coded - Design and coding required

Colors

Designer to choose colors to be used in the design.

Requirements
Must have
• A home page A section of% 26 # 233; writing the services offered% 26 # 233; es by Velmora with the possibility% 26 # 233; d% 26 # 39; add sub-headings which can% 26 # 234; be displayed% 26 # 233; e or hidden% 26 # 233; e A page with the r% 26 # 233; f% 26 # 233; which can be displayed% 26 # 233; e or hidden% 26 # 233; e A page of% 26 # 233; writing l% 26 # 39;% 26 # 233; team A page with form contact, addresses and int card% 26 # 233; gr% 26 # 233; e The site must% 26 # 234; be low% 26 # 233; on a CMS allowing% 26 # 39;% 26 # 234; to be autonomous in modifying the website The possibility% 26 # 233; to be able to translate the site into several languages (FR, EN, DE, IT, NL, ...)

```html
<!DOCTYPE html>
<html lang="en">
<head>
<meta charset="utf-8">
<title>Velmora – Market Research and Logistics</title>
<link href="https://fonts.googleapis.com/css2?family=Barlow:wght@300;400;600;700&family=Lato:wght@400;700&display=swap" rel="stylesheet">
<style>
:root{
  --navy:#1b2d40;
  --navy-deep:#16263a;
  --hero-a:#2c4660;
  --hero-b:#3d5d78;
  --slate:#a3afc2;
  --slate-soft:#e3e7ed;
  --line:#8fa3c0;
  --text:#333a44;
  --white:#ffffff;
}
*{margin:0;padding:0;box-sizing:border-box}
html,body{width:1200px;height:3102px;overflow:hidden;background:var(--white)}
body{position:relative;font-family:"Lato",sans-serif;color:var(--text)}
.abs{position:absolute}
.heading{font-family:"Barlow",sans-serif;font-weight:700;color:var(--navy);font-size:35px;letter-spacing:.3px}

/* header */
.site-header{position:absolute;left:0;top:0;width:1200px;height:90px;background:var(--white)}
.brand{position:absolute;left:102px;top:24px;display:flex;align-items:center;gap:22px}
.brand-square{width:44px;height:44px;border-radius:9px;background:var(--navy)}
.brand-name{font-family:"Lato",sans-serif;font-weight:400;font-size:36px;letter-spacing:5px;color:var(--navy)}
.main-nav a{position:absolute;top:36px;font-family:"Lato",sans-serif;font-weight:700;font-size:15px;color:#4f6680;text-decoration:none;transform:translateX(-50%);white-space:nowrap}
.main-nav a.is-active{color:var(--navy)}
.main-nav a.is-active::after{content:"";position:absolute;left:0;right:0;top:28px;height:3px;background:var(--navy)}

/* hero */
.hero{position:absolute;left:0;top:90px;width:1200px;height:670px;clip-path:path("M0 0 H1200 V560 L640 662 Q600 672 560 662 L0 560 Z");background:linear-gradient(180deg,#2a4158 0%,#4a6a86 35%,#2f4b65 60%,#3c5c77 100%)}
.hero-title{position:absolute;left:0;width:1200px;text-align:center;color:var(--white);font-family:"Barlow",sans-serif}
.hero-kicker{top:212px;font-size:29px;font-weight:300;letter-spacing:.5px}
.hero-main{top:257px;font-size:60px;font-weight:700;line-height:60px}
.hero-sub{top:317px;font-size:60px;font-weight:300;line-height:60px}
.hero-arrow{position:absolute;top:255px}

/* about */
.about-visual{position:absolute;left:166px;top:818px;width:376px;height:374px;border-radius:120px;background:linear-gradient(135deg,#7a6a5c,#c9c4bb 45%,#6b7d8c)}
.about-text{position:absolute;left:596px;width:500px;font-size:19px;line-height:25px;color:var(--text)}
.btn{position:absolute;display:flex;align-items:center;justify-content:center;font-family:"Lato",sans-serif;font-weight:700;font-size:17px;text-decoration:none;border-radius:0 24px 0 24px}
.btn-dark{background:var(--navy);color:var(--white)}
.btn-light{background:var(--slate);color:var(--navy)}

/* services */
.services{position:absolute;left:0;top:1273px;width:1200px;height:553px;background:linear-gradient(100deg,#d8dde4,#eef0f3 40%,#e2e6ec 70%,#d5dbe3)}
.service{position:absolute}
.service-shape{position:absolute;left:50%;top:50%;transform:translate(-50%,-50%) rotate(45deg);border-radius:70px}
.service-body{position:relative;text-align:center;color:var(--white)}
.service-name{font-family:"Lato",sans-serif;font-weight:700;font-size:19px;margin-top:8px}
.service-desc{font-size:13px;line-height:20px;margin-top:10px}

/* team */
.member{position:absolute;top:1944px;width:226px;height:273px;border:2px solid var(--line);background:var(--white);text-align:center}
.member-photo{position:absolute;left:10px;top:8px;width:202px;height:190px;background:linear-gradient(180deg,#f3f4f6,#dfe3e8)}
.member-name{position:absolute;left:0;right:0;top:223px;font-size:15px;font-weight:700;color:#2c3440}
.member-role{position:absolute;left:0;right:0;top:246px;font-size:12px;font-weight:700;color:#2c3440}

/* contact */
.contact{position:absolute;left:0;top:2391px;width:1200px;height:711px;background:linear-gradient(180deg,#2a3f55 0%,#1d3147 50%,#213a52 100%)}
.contact-label{position:absolute;left:0;font-size:17px;font-weight:700;color:var(--white)}
.contact-value{position:absolute;left:0;font-size:18px;color:var(--white)}
.field{position:absolute;left:626px;width:464px;border:1.5px solid #c6cfdb;color:#e4e9ef;font-size:16px;padding:12px 0 0 21px}
.footer{position:absolute;left:0;top:2880px;width:1200px;height:222px}
.footer-nav a{position:absolute;top:93px;transform:translateX(-50%);font-weight:700;font-size:17px;color:var(--navy);text-decoration:none}
.social{position:absolute;top:148px;width:36px;height:36px;border-radius:50%;background:var(--navy)}
</style>
</head>
<body>

<header class="site-header">
  <div class="brand"><span class="brand-square"></span><span class="brand-name">VELMORA</span></div>
  <nav class="main-nav">
    <a href="#" class="is-active" style="left:510px">HOME</a>
    <a href="#" style="left:608px">ABOUT US</a>
    <a href="#" style="left:735px">OUR SERVICES</a>
    <a href="#" style="left:845px">TEAM</a>
    <a href="#" style="left:939px">CONTACT</a>
    <a href="#" style="left:1033px">EN <svg width="12" height="9" viewBox="0 0 12 9"><path d="M1 2l5 5 5-5" fill="none" stroke="#1b2d40" stroke-width="2"/></svg></a>
  </nav>
</header>

<section class="hero" role="img" aria-label="Snow-capped mountain range above a calm lake, tinted deep blue">
  <p class="hero-title hero-kicker">WELCOME TO VELMORA</p>
  <h1 class="hero-title hero-main">MARKET RESEARCH</h1>
  <p class="hero-title hero-sub">AND LOGISTICS</p>
  <svg class="hero-arrow" style="left:70px" width="28" height="56" viewBox="0 0 28 56"><path d="M26 2L3 28l23 26" fill="none" stroke="#fff" stroke-width="2.5"/></svg>
  <svg class="hero-arrow" style="left:1106px" width="28" height="56" viewBox="0 0 28 56"><path d="M2 2l23 26L2 54" fill="none" stroke="#fff" stroke-width="2.5"/></svg>
</section>

<section class="about">
  <div class="about-visual" role="img" aria-label="Desk with laptop, printed charts and sticky notes"></div>
  <h2 class="heading abs" style="left:593px;top:843px">ABOUT VELMORA</h2>
  <p class="about-text" style="top:909px">Pellentesque faucibus Ut accumsan ultricies elit Maecenas at justo id velit placerat molestie Donec dictum lectus non odio Cras a ante vitae enim iaculis aliquam</p>
  <p class="about-text" style="top:1013px">Mauris nunc quam venenatis nec euismod sit amet egestas placerat est Pellentesque habitant morbi tristique senectus et netus et malesuada fames ac turpis egestas Cras id elit</p>
  <a href="#" class="btn btn-dark" style="left:598px;top:1120px;width:181px;height:51px">LEARN MORE</a>
</section>

<section class="services" role="img" aria-label="Faded photo of a team meeting around a table">
  <h2 class="heading abs" style="left:0;width:1200px;text-align:center;top:63px">OUR SERVICES</h2>

  <div class="service" style="left:258px;top:294px">
    <div class="service-shape" style="width:222px;height:222px;background:var(--slate)"></div>
    <div class="service-body" style="position:absolute;left:-110px;top:-90px;width:220px">
      <svg width="60" height="58" viewBox="0 0 60 58" fill="none" stroke="#fff" stroke-width="2"><circle cx="30" cy="30" r="22"/><circle cx="30" cy="30" r="14"/><path d="M24 36v-6M29 36v-10M34 36v-8"/><path d="M8 6h10M4 12h8"/></svg>
      <div class="service-name">MARKET RESEARCH</div>
      <div class="service-desc" style="color:#eef1f5">Suspendisse quam leo molestie<br>sed luctus quis feugiat in</div>
      <svg style="margin-top:18px" width="30" height="30" viewBox="0 0 30 30" fill="none" stroke="#fff" stroke-width="2.5"><path d="M15 2v25M4 16l11 11 11-11"/></svg>
    </div>
  </div>

  <div class="service" style="left:598px;top:294px">
    <div class="service-shape" style="width:252px;height:252px;background:var(--navy)"></div>
    <div class="service-body" style="position:absolute;left:-130px;top:-105px;width:260px">
      <svg width="72" height="72" viewBox="0 0 72 72" fill="none" stroke="#fff" stroke-width="2"><path d="M36 24l12 6v13l-12 6-12-6V30z"/><path d="M24 30l12 6 12-6M36 36v13"/><path d="M36 4v12M36 56v12M4 36h12M56 36h12M13 13l8 8M59 13l-8 8M13 59l8-8M59 59l-8-8"/></svg>
      <div class="service-name">LOGISTICS</div>
      <div class="service-desc">Allamcorper est eget tempor cursus neque<br>mi consectetuer mi a ultricies massa est<br>sed nisl Class aptent taciti</div>
      <svg style="margin-top:12px" width="30" height="30" viewBox="0 0 30 30" fill="none" stroke="#fff" stroke-width="2.5"><path d="M15 2v25M4 16l11 11 11-11"/></svg>
    </div>
  </div>

  <div class="service" style="left:940px;top:294px">
    <div class="service-shape" style="width:222px;height:222px;background:var(--slate)"></div>
    <div class="service-body" style="position:absolute;left:-110px;top:-92px;width:220px">
      <svg width="62" height="62" viewBox="0 0 62 62" fill="none" stroke="#fff" stroke-width="2"><circle cx="31" cy="31" r="28"/><path d="M31 3v56M31 31L10 50"/><text x="10" y="24" fill="#fff" stroke="none" font-size="11" font-family="Lato">TAX</text><text x="36" y="40" fill="#fff" stroke="none" font-size="16" font-family="Lato">%</text><text x="16" y="52" fill="#fff" stroke="none" font-size="13" font-family="Lato">$</text></svg>
      <div class="service-name">TAX REPRESENTATION</div>
      <div class="service-desc" style="color:#eef1f5">Suspendisse quam leo molestie<br>sed luctus quis feugiat in</div>
      <svg style="margin-top:18px" width="30" height="30" viewBox="0 0 30 30" fill="none" stroke="#fff" stroke-width="2.5"><path d="M15 2v25M4 16l11 11 11-11"/></svg>
    </div>
  </div>
</section>

<section class="team">
  <h2 class="heading abs" style="left:0;width:1200px;text-align:center;top:1870px">OUR TEAM</h2>
  <article class="member" style="left:118px"><div class="member-photo" role="img" aria-label="Portrait of team member"></div><div class="member-name">MEMBER NAME</div><div class="member-role">Post Designation</div></article>
  <article class="member" style="left:365px"><div class="member-photo" role="img" aria-label="Portrait of team member"></div><div class="member-name" style="top:219px">MEMBER NAME</div><div class="member-role" style="top:242px">Post Designation</div></article>
  <article class="member" style="left:612px"><div class="member-photo" role="img" aria-label="Portrait of team member"></div><div class="member-name" style="top:219px">MEMBER NAME</div><div class="member-role" style="top:242px">Post Designation</div></article>
  <article class="member" style="left:859px"><div class="member-photo" role="img" aria-label="Portrait of team member"></div><div class="member-name" style="top:219px">MEMBER NAME</div><div class="member-role" style="top:242px">Post Designation</div></article>
  <a href="#" class="btn btn-dark" style="left:508px;top:2268px;width:180px;height:51px">LEARN MORE</a>
</section>

<section class="contact" role="img" aria-label="Harbour with cranes and cargo ship at dusk, tinted navy">
  <h2 class="heading abs" style="left:166px;top:112px;color:var(--white);font-size:33px">CONTACT US</h2>

  <svg class="abs" style="left:170px;top:178px" width="40" height="44" viewBox="0 0 40 44" fill="none" stroke="#fff" stroke-width="1.8"><path d="M20 38s-11-12-11-21a11 11 0 0 1 22 0c0 9-11 21-11 21z"/><circle cx="20" cy="17" r="4"/><ellipse cx="20" cy="39" rx="16" ry="4"/></svg>
  <div class="abs" style="left:234px;top:175px"><div class="contact-label" style="top:0">ADDRESS</div><div class="contact-value" style="top:24px;white-space:nowrap">48 Lakeside Row, Suite 3B, Brookhaven 20417</div></div>

  <svg class="abs" style="left:170px;top:262px" width="42" height="42" viewBox="0 0 42 42" fill="none" stroke="#fff" stroke-width="1.8"><path d="M9 3l7 9-4 5c3 6 7 10 13 13l5-4 9 7-4 6c-16-1-30-15-31-31z"/></svg>
  <div class="abs" style="left:232px;top:267px"><div class="contact-label" style="top:0;white-space:nowrap">PHONE NUMBER</div><div class="contact-value" style="top:24px">555.014.2270</div></div>

  <svg class="abs" style="left:172px;top:360px" width="42" height="32" viewBox="0 0 42 32" fill="none" stroke="#fff" stroke-width="1.8"><rect x="2" y="2" width="38" height="28"/><path d="M2 2l19 16L40 2M2 30l14-13M40 30L26 17"/></svg>
  <div class="abs" style="left:232px;top:358px"><div class="contact-label" style="top:0;white-space:nowrap">EMAIL US</div><div class="contact-value" style="top:24px;white-space:nowrap">hello@velmora-consult.example</div></div>

  <div class="field" style="top:114px;height:42px">Name</div>
  <div class="field" style="top:164px;height:42px">Email</div>
  <div class="field" style="top:214px;height:42px">Phone</div>
  <div class="field" style="top:267px;height:89px">Message</div>
  <a href="#" class="btn btn-light" style="left:630px;top:371px;width:180px;height:51px">SUBMIT NOW</a>
</section>

<footer class="footer">
  <svg class="abs" style="left:0;top:0" width="1200" height="222" viewBox="0 0 1200 222"><path d="M0 111L600 20 1200 111V222H0z" fill="#fff"/></svg>
  <span class="abs" style="left:565px;top:0;width:50px;height:50px;border-radius:12px;background:var(--navy);border:3px solid #fff"></span>
  <nav class="footer-nav">
    <a href="#" style="left:346px">HOME</a>
    <a href="#" style="left:454px">ABOUT US</a>
    <a href="#" style="left:595px">OUR SERVICES</a>
    <a href="#" style="left:716px">TEAM</a>
    <a href="#" style="left:820px">CONTACT</a>
  </nav>
  <p class="abs" style="left:0;width:1200px;top:126px;text-align:center;font-family:Arial,sans-serif;font-size:13px;color:#5c6878">© 2020 Company Name &nbsp;All right reserved</p>
  <span class="social" style="left:521px" aria-label="Social link"></span>
  <span class="social" style="left:566px" aria-label="Social link"></span>
  <span class="social" style="left:611px" aria-label="Social link"></span>
</footer>

</body>
</html>
```